Move the hackers to Wordpress

Yep, we want to move https://www.tallowmarsh.com/ to Wordpress. It'll make it easier to update and add content. I'd like mostly the same look, but I'm not stuck with it.
Updates

DO NOT RESPOND OUTSIDE OF PIXEL HARBOR OR CONTACT US DIRECTLY.

Industry/Entity Type

Computer Security

Coding

Coded - Design and coding required

Font styles to use
Sans Serif

Colors
ec1f27

Requirements
Must have
• What I do want is:
• 1. Similar look to the existing site
• 2. Needs to work on one of the Wordpress hosting sites. I do NOT want to run my own Wordpress server.
• 3. Keep the animation in the top panel.
• 4. Mobile support
• The rest can be changed as needed.
Nice to have
• I like the transitions when the "services" panel shows up. Not stuck on it, but it is a nice touch.

```html
<!DOCTYPE html>
<html lang="en">
<head>
<meta charset="utf-8">
<title>Tallow Marsh Information Security</title>
<link rel="stylesheet" href="https://fonts.googleapis.com/css2?family=Oswald:wght@300;400&family=Raleway:wght@400;500&family=Roboto:wght@400;500;700&display=swap">
<style>
:root{
  --red:#ec1f27;
  --red-dark:#c9161d;
  --ink:#222;
  --body:#444;
  --dark:#111;
  --charcoal:#2b2b2b;
  --white:#fff;
  --grey:#e9e9e9;
}
*{box-sizing:border-box;margin:0;padding:0}
html,body{width:1200px;height:3622px;overflow:hidden}
body{position:relative;background:var(--white);font-family:"Roboto",Arial,sans-serif;color:var(--body)}
.abs{position:absolute}
.center{text-align:center}

/* hero */
.hero{left:0;top:0;width:1200px;height:660px;background:radial-gradient(ellipse at 50% 45%,#3c3c3c 0%,#262626 60%,#1b1b1b 100%)}
.brand{left:165px;top:26px;display:flex;align-items:center;gap:12px}
.brand-mark{width:38px;height:38px;background:var(--red)}
.brand-name{font:500 30px/1 "Raleway",sans-serif;color:var(--white);letter-spacing:2px}
.brand-sub{font:400 11px/1 "Roboto",sans-serif;color:var(--white);letter-spacing:3px;margin-top:5px}
.topbar{left:748px;top:0;width:300px;height:34px;background:var(--white);border-radius:0 0 0 18px;display:flex;align-items:center;justify-content:flex-end;gap:8px;padding-right:12px}
.topbar .phone{font:700 18px "Roboto",sans-serif;color:var(--ink);margin-right:6px;display:flex;align-items:center;gap:6px}
.social{width:22px;height:22px;border-radius:50%;background:var(--red)}
.social.dark{background:var(--ink)}
.nav{right:163px;top:58px;display:flex;gap:26px;font:400 16px "Roboto",sans-serif;color:var(--white)}
.hero-title{left:0;width:1200px;top:258px;font:400 52px/68px "Oswald",sans-serif;color:var(--white);text-align:center}
.hero-title em{font-style:normal;color:var(--red)}

h2.section{font:400 38px/1 "Raleway",sans-serif;color:var(--ink);width:1200px;left:0;text-align:center}
h2.section span{color:var(--red)}
.rule{width:38px;height:3px;background:var(--red);left:581px}

/* what we do */
.lead{left:0;width:1200px;top:768px;font:400 15px "Roboto",sans-serif;color:var(--red)}
.intro{left:180px;width:840px;top:796px;font:400 13.5px/22px "Roboto",sans-serif;text-align:center}

/* services */
.svc-icon{left:588px;top:926px;width:24px;height:30px;background:var(--red)}
.card{width:290px;padding:0 22px;text-align:center}
.card.red{background:var(--red);color:var(--white);box-shadow:0 6px 14px rgba(0,0,0,.25)}
.card.plain{background:var(--white);color:var(--ink)}
.card svg{display:block;margin:24px auto 14px}
.card h3{font:400 19px/23px "Raleway",sans-serif}
.card.plain h3.hi{color:var(--red)}
.card hr{border:0;height:1px;background:currentColor;opacity:.5;margin:10px 10px 12px}
.card p{font:400 12px/19px "Roboto",sans-serif}

/* about */
.about-band{left:0;top:1823px;width:1200px;height:297px;background:linear-gradient(180deg,#2c2c2c,#4a4a4a 70%,#3a3a3a)}
.about-title{top:1882px;color:var(--white)!important}
.about-text{left:0;width:1200px;top:1946px;font:400 15px "Roboto",sans-serif;color:var(--white)}
.video{left:210px;top:1988px;width:780px;height:428px;border:2px solid var(--red);padding:6px;background:var(--white)}
.video-scene{position:absolute;left:6px;top:6px;right:6px;bottom:6px;background:linear-gradient(160deg,#4b5466 0%,#2a2f3a 45%,#6a6f7c 100%)}
.play{position:absolute;left:355px;top:168px;width:60px;height:60px;border-radius:50%;background:rgba(255,255,255,.85);display:flex;align-items:center;justify-content:center}
.controls{position:absolute;left:16px;right:16px;bottom:14px;height:36px;background:rgba(20,20,20,.7);display:flex;align-items:center;gap:14px;padding:0 14px;color:var(--white);font:500 15px "Roboto",sans-serif}
.track{flex:1;height:6px;background:#777;border-radius:3px;position:relative}
.track::before{content:"";position:absolute;left:0;top:0;width:70px;height:6px;background:#ddd;border-radius:3px}

/* why */
.why{left:0;top:2467px;width:1200px;height:435px;background:var(--dark)}
.why-title{top:2530px;color:var(--white)!important}
.why-label{font:400 15px "Roboto",sans-serif;color:var(--white);width:200px}
.why-label.l{text-align:right}
.why-icon{width:76px;height:76px;border-radius:50%;background:var(--red);border:3px solid var(--white);display:flex;align-items:center;justify-content:center}
.arc{left:425px;top:2727px;width:350px;height:175px;border-radius:175px 175px 0 0;background:var(--white);border:10px solid #bdbdbd;border-bottom:0}
.arc-brand{left:455px;top:2830px;width:290px;text-align:center;font:500 24px "Raleway",sans-serif;color:var(--red);letter-spacing:2px}

/* testimonials */
.quote{left:574px;top:3022px;width:52px;height:52px;border-radius:50%;border:2px solid var(--red);color:var(--red);font:700 36px/60px "Roboto",sans-serif;text-align:center}
.testi{left:0;width:1200px;font:italic 400 14.5px "Roboto",sans-serif;color:var(--ink)}
.arrow{top:3076px}

/* contact */
.contact{left:0;top:3230px;width:1200px;height:348px;background:var(--red)}
.contact-title{left:164px;top:3280px;font:400 22px/1.2 "Raleway",sans-serif;color:var(--white)}
.c-row{left:164px;display:flex;gap:18px;color:var(--white);font:400 12px/17px "Roboto",sans-serif}
.c-row b{font-weight:700}
.field{background:rgba(255,255,255,.28);color:var(--white);font:400 11px "Roboto",sans-serif;padding:5px 10px}
.submit{left:640px;top:3494px;width:84px;height:36px;background:var(--dark);color:var(--white);font:700 15px/36px "Roboto",sans-serif;text-align:center}
.footer{left:0;top:3578px;width:1200px;height:44px;background:var(--charcoal);color:var(--white);font:400 12px/44px "Roboto",sans-serif;padding:0 164px;display:flex;justify-content:space-between}
.footer .fb{font:500 16px/44px "Raleway",sans-serif;color:var(--red);letter-spacing:2px}
</style>
</head>
<body>

<section class="abs hero" role="img" aria-label="Dark background with an animated network of red nodes joined by thin grey lines"></section>
<div class="abs brand">
  <div class="brand-mark"></div>
  <div><div class="brand-name">TALLOW MARSH</div><div class="brand-sub">INFORMATION SECURITY</div></div>
</div>
<div class="abs topbar">
  <span class="phone"><svg width="18" height="18" viewBox="0 0 24 24"><circle cx="12" cy="12" r="12" fill="#ec1f27"/><path d="M8 6l2 0 1 3-1.5 1a7 7 0 0 0 4 4l1-1.5 3 1v2a1.5 1.5 0 0 1-1.5 1.5A10 10 0 0 1 6.5 7.5 1.5 1.5 0 0 1 8 6z" fill="#fff"/></svg>+1.555.014.2290</span>
  <span class="social"></span><span class="social dark"></span><span class="social dark"></span>
</div>
<nav class="abs nav"><span>What We Do</span><span>Services</span><span>Blog</span><span>Press</span><span>Contact Us</span></nav>
<h1 class="abs hero-title"><em>OFFENSIVE</em> SERVICES<br>FROM <em>OFFENSIVE</em> MINDS</h1>

<h2 class="abs section" style="top:706px">What <span>We Do</span></h2>
<div class="abs rule" style="top:750px"></div>
<p class="abs lead center">We are an information security company focusing on real world threats.</p>
<p class="abs intro">Tallow Marsh is an information security consulting company that concentrates on the latest threats to organizations today. We perform in-depth analysis, determine organization/business risk, and find the vulnerabilities before the bad guys do. Our team includes internationally renowned experts who have been featured in international news outlets and conferences, including The Harbor Ledger, The Northgate Post, a Meridian News Network Documentary.</p>

<div class="abs svc-icon"></div>
<h2 class="abs section" style="top:962px">Our <span>Services</span></h2>
<div class="abs rule" style="top:1006px"></div>

<div class="abs card red" style="left:164px;top:1033px;height:367px">
  <svg width="70" height="56" viewBox="0 0 70 56" fill="none" stroke="#fff" stroke-width="3"><rect x="4" y="4" width="44" height="32"/><path d="M18 46h16M26 36v10"/><rect x="52" y="16" width="14" height="26"/></svg>
  <h3>Internal Pivot Assessment<br>&amp; Post Exploitation</h3><hr>
  <p>We start as low privilege user &amp; attempt to move through the network in an attempt to access the data that matters to you. This is a simulation of a rogue trusted insider or a compromised internal host. We determine your risk when the egg shell is cracked. Even a seemingly insignificant compromise can have big consequences &amp; our goal is to demonstrate the risk.</p>
</div>
<div class="abs card plain" style="left:454px;top:1033px;height:367px">
  <svg width="70" height="56" viewBox="0 0 70 56" fill="#ec1f27"><circle cx="35" cy="14" r="10"/><path d="M18 52c0-12 8-20 17-20s17 8 17 20z"/><circle cx="14" cy="20" r="7"/><circle cx="56" cy="20" r="7"/></svg>
  <h3 class="hi">Red Team Adversary<br>Simulation</h3><hr>
  <p>A goal-based assessment where we attack just like a real world adversary. This includes external attacks and targeted phishing to demonstrate the real risk to<br>your data.</p>
</div>
<div class="abs card red" style="left:744px;top:1033px;height:367px">
  <svg width="70" height="56" viewBox="0 0 70 56" fill="none" stroke="#fff" stroke-width="3"><rect x="4" y="20" width="30" height="22"/><rect x="42" y="14" width="22" height="34"/><path d="M10 10h50M34 31h8"/></svg>
  <h3>Penetration Testing &amp;<br>Vulnerability Assessments</h3><hr>
  <p>This includes vulnerability scans of the in-scope systems where we manually verify issues and exploit any issues found. We report on the issues that actually have a real risk to your organization.</p>
</div>
<div class="abs card plain" style="left:164px;top:1412px;height:363px">
  <svg width="70" height="56" viewBox="0 0 70 56" fill="none" stroke="#222" stroke-width="3"><circle cx="35" cy="28" r="24"/><circle cx="35" cy="28" r="14"/><circle cx="35" cy="28" r="4"/><path d="M35 28l16-16"/></svg>
  <h3>Advanced Product,<br>Hardware &amp; RF Testing</h3><hr>
  <p>This is a highly customized assessment designed for you and your hardware. Depending on the product we will analyze custom RF protocols, reverse engineer OS and firmware, and analyze and fuzz network protocols. We have tested a range of products from toys to security products.</p>
</div>
<div class="abs card red" style="left:454px;top:1400px;height:375px">
  <svg width="70" height="56" viewBox="0 0 70 56" fill="none" stroke="#fff" stroke-width="3"><rect x="30" y="8" width="34" height="26"/><rect x="42" y="18" width="10" height="9"/><path d="M44 18v-4h6v4"/><circle cx="14" cy="38" r="7"/><path d="M20 34l12-10"/></svg>
  <h3>Web Application<br>Penetration Testing</h3><hr>
  <p>Our team will perform an in-depth analysis of your web application to find vulnerabilities related to programming errors, misconfiguration, and application architectural issues. We will perform automated and manual runtime analysis of your application. We create custom test cases to fuzz your application and find the faults before the bad guys do.</p>
</div>
<div class="abs card plain" style="left:744px;top:1412px;height:363px">
  <svg width="70" height="56" viewBox="0 0 70 56" fill="none" stroke="#222" stroke-width="3"><rect x="20" y="4" width="26" height="46" rx="3"/><rect x="38" y="24" width="18" height="18" fill="#999" stroke="none"/><path d="M30 44h6"/></svg>
  <h3>Mobile Application<br>Assessment</h3><hr>
  <p>We look at your mobile application and the associated infrastructure to find configuration weaknesses, server-side issues, insecure authentication and access control, and other issues related to the latest attacks on mobile applications.</p>
</div>

<section class="abs about-band" role="img" aria-label="Dim city skyline photograph behind the About Us heading"></section>
<h2 class="abs section about-title">About Us</h2>
<div class="abs rule" style="top:1926px"></div>
<p class="abs about-text center">We focus on hacking. This is our passion. We find the vulnerabilities before the bad guys do.</p>
<div class="abs video">
  <div class="video-scene" role="img" aria-label="Video still: close-up of a person wearing glasses looking at a screen"></div>
  <div class="play"><svg width="22" height="24" viewBox="0 0 22 24"><path d="M2 1l19 11-19 11z" fill="#ec1f27"/></svg></div>
  <div class="controls">
    <svg width="14" height="16" viewBox="0 0 14 16"><path d="M0 0l14 8-14 8z" fill="#fff"/></svg>
    <div class="track"></div><span>0:02</span>
    <svg width="20" height="16" viewBox="0 0 20 16"><path d="M0 5h5l6-5v16l-6-5H0z" fill="#aaa"/></svg>
    <svg width="16" height="16" viewBox="0 0 16 16" fill="none" stroke="#aaa" stroke-width="2"><path d="M1 6V1h5M10 1h5v5M15 10v5h-5M6 15H1v-5"/></svg>
  </div>
</div>

<section class="abs why"></section>
<h2 class="abs section why-title">Why Choose Us</h2>
<div class="abs rule" style="top:2574px"></div>
<div class="abs arc"></div>
<div class="abs arc-brand">TALLOW MARSH<div style="font:400 9px 'Roboto',sans-serif;letter-spacing:3px;color:#222;margin-top:4px">INFORMATION SECURITY</div></div>

<div class="abs why-label l" style="left:190px;top:2640px">Unbiased Recommendations</div>
<div class="abs why-icon" style="left:498px;top:2637px"><svg width="34" height="30" viewBox="0 0 34 30" fill="#fff"><path d="M3 3h28v18H14l-7 6v-6H3z"/></svg></div>
<div class="abs why-icon" style="left:623px;top:2637px"><svg width="30" height="34" viewBox="0 0 30 34" fill="#fff"><circle cx="15" cy="10" r="8"/><path d="M2 34c0-10 6-15 13-15s13 5 13 15z"/></svg></div>
<div class="abs why-label" style="left:712px;top:2640px">Expert Guidance</div>
<div class="abs why-label l" style="left:178px;top:2710px">Proactive Service</div>
<div class="abs why-icon" style="left:392px;top:2687px"><svg width="32" height="32" viewBox="0 0 32 32" fill="none" stroke="#fff" stroke-width="4"><circle cx="16" cy="16" r="8"/><path d="M16 2v6M16 24v6M2 16h6M24 16h6"/></svg></div>
<div class="abs why-icon" style="left:730px;top:2685px"><svg width="30" height="30" viewBox="0 0 30 30" fill="none" stroke="#fff" stroke-width="3"><rect x="3" y="5" width="24" height="22"/><path d="M3 12h24M9 2v6M21 2v6"/></svg></div>
<div class="abs why-label" style="left:818px;top:2714px">Business-Minded Solution</div>
<div class="abs why-label l" style="left:130px;top:2814px">Superior Advice</div>
<div class="abs why-icon" style="left:343px;top:2784px"><svg width="30" height="32" viewBox="0 0 30 32" fill="#fff"><circle cx="15" cy="13" r="9"/><rect x="11" y="23" width="8" height="6"/></svg></div>
<div class="abs why-icon" style="left:783px;top:2786px"><svg width="30" height="32" viewBox="0 0 30 32" fill="#fff"><circle cx="11" cy="9" r="6"/><path d="M1 30c0-9 4-13 10-13s10 4 10 13z"/><circle cx="23" cy="18" r="6" fill="none" stroke="#fff" stroke-width="3"/></svg></div>
<div class="abs why-label" style="left:870px;top:2804px;width:120px">Efficient Legal<br>Solutions</div>

<h2 class="abs section" style="top:2958px">Clients Testimonials</h2>
<div class="abs rule" style="top:3002px"></div>
<div class="abs quote">&ldquo;</div>
<p class="abs testi center" style="top:3098px">I read the report yesterday.</p>
<p class="abs testi center" style="top:3125px">This is one of the best-written, actionable pentest reports I've ever seen.</p>
<p class="abs testi center" style="top:3173px;font-style:normal;color:#555">D.H. (Undisclosed Organization)</p>
<svg class="abs arrow" style="left:140px" width="24" height="44" viewBox="0 0 24 44" fill="none" stroke="#bbb" stroke-width="2"><path d="M22 2L2 22l20 20"/></svg>
<svg class="abs arrow" style="left:1036px" width="24" height="44" viewBox="0 0 24 44" fill="none" stroke="#bbb" stroke-width="2"><path d="M2 2l20 20-20 20"/></svg>

<section class="abs contact"></section>
<h4 class="abs contact-title">Contact Us</h4>
<div class="abs rule" style="left:164px;top:3312px;background:#fff;width:30px"></div>
<div class="abs c-row" style="top:3328px"><svg width="16" height="22" viewBox="0 0 16 22"><path d="M8 0a8 8 0 0 1 8 8c0 6-8 14-8 14S0 14 0 8a8 8 0 0 1 8-8z" fill="#fff"/><circle cx="8" cy="8" r="3" fill="#ec1f27"/></svg><div><b>TALLOW MARSH INFORMATION SECURITY</b><br>Street Name, City Name<br>State Zipcode</div></div>
<div class="abs c-row" style="top:3418px"><svg width="16" height="16" viewBox="0 0 24 24"><path d="M5 2h4l2 5-2.5 2a11 11 0 0 0 6.5 6.5L17 13l5 2v4a3 3 0 0 1-3 3A18 18 0 0 1 2 5a3 3 0 0 1 3-3z" fill="#fff"/></svg><span>+1.555.014.2290</span></div>
<div class="abs c-row" style="top:3462px"><svg width="16" height="14" viewBox="0 0 16 14"><rect width="16" height="14" fill="#fff"/><path d="M0 0l8 7 8-7" fill="none" stroke="#ec1f27" stroke-width="1.5"/></svg><span>contact@tallowmarsh.com</span></div>

<div class="abs field" style="left:640px;top:3276px;width:398px;height:32px">Name</div>
<div class="abs field" style="left:640px;top:3322px;width:196px;height:32px">Email</div>
<div class="abs field" style="left:842px;top:3322px;width:196px;height:32px">Mobile</div>
<div class="abs field" style="left:640px;top:3366px;width:398px;height:110px">Message</div>
<div class="abs submit">Submit</div>

<footer class="abs footer"><span>Copyright &copy; 2018 Tallow Marsh Information Security &nbsp;|&nbsp; All Rights Reserved.</span><span class="fb">TALLOW MARSH</span></footer>

</body>
</html>
```